Brightwell Electrical and Air conditioning services needs Designer Van Signage.

Brightwell Electrical and Air conditioning company needs a Van signage designed to give customers a professional image of the business. Attached are some sample design that we will be interested in. Do not need full van wrap, Back Half should be ok.

Industry/Entity Type

Electrical, Air conditioning, & Plumbing

Requirements
Must have
• 24 hour emergency service. Electrical , Air conditioning & Plumbing ideas. Please show all around van. front back and 2 sides.
Nice to have
• Please use mobile number: 0437205816, email: info@brightwellelectrical-example.com.au, Web: www.brightwellelectrical-example.com.au.
Should not have
• Full van wrap

```html
<!DOCTYPE html>
<html lang="en">
<head>
<meta charset="utf-8">
<title>Brightwell Van Signage</title>
<link href="https://fonts.googleapis.com/css2?family=Poppins:ital,wght@0,500;0,600;0,700;1,700&display=swap" rel="stylesheet">
<style>
  :root {
    --bg: #ecedef;
    --panel: #ffffff;
    --edge: #d3d5d9;
    --orange: #ec8a2c;
    --red: #dc1f26;
    --blue: #1f59a8;
    --white: #ffffff;
  }
  html, body { margin: 0; padding: 0; overflow: hidden; }
  body {
    width: 1200px; height: 1200px;
    background: var(--bg);
    font-family: "Poppins", sans-serif;
  }
  .signage { width: 1200px; height: 1200px; position: relative; }
  .side-view { position: absolute; left: 50px; width: 1100px; height: 480px; }
  .side-view--a { top: 70px; }
  .side-view--b { top: 650px; }
  .wordmark { font-weight: 700; fill: var(--orange); font-size: 96px; }
  .services { font-weight: 700; font-size: 26px; }
  .svc-electrical { fill: var(--red); }
  .svc-air { fill: var(--blue); }
  .svc-plumbing { fill: var(--orange); }
  .phone { font-weight: 600; letter-spacing: 5px; }
  .web { font-weight: 500; fill: var(--white); letter-spacing: 1px; }
  .badge-hours { font-weight: 700; font-style: italic; fill: var(--blue); }
  .badge-label { font-weight: 700; font-style: italic; }
</style>
</head>
<body>
<main class="signage">

  <!-- Layout A: angled bands -->
  <svg class="side-view side-view--a" viewBox="0 0 1100 480" aria-label="Van side layout with angled bands">
    <defs>
      <clipPath id="panel-a"><rect x="0" y="0" width="1100" height="480" rx="40"/></clipPath>
    </defs>
    <g clip-path="url(#panel-a)">
      <rect class="panel-body" x="0" y="0" width="1100" height="480" fill="var(--panel)"/>
      <polygon class="swoosh" points="0,150 600,40 0,190" fill="var(--orange)"/>
      <polygon class="band-blue" points="0,400 1100,250 1100,302 0,452" fill="var(--blue)"/>
      <polygon class="band-red" points="0,452 1100,302 1100,480 0,480" fill="var(--red)"/>
      <circle class="brand-dot" cx="930" cy="150" r="110" fill="var(--orange)"/>
    </g>
    <rect x="0.5" y="0.5" width="1099" height="479" rx="40" fill="none" stroke="var(--edge)"/>

    <g class="badge">
      <text class="badge-label" x="20" y="262" font-size="17" fill="var(--blue)">Emergency</text>
      <text class="badge-label" x="44" y="282" font-size="17" fill="var(--red)">Services</text>
      <text class="badge-hours" x="128" y="268" font-size="40">24/7</text>
    </g>

    <text class="wordmark" x="250" y="250">Brightwell</text>
    <text class="services">
      <tspan class="svc-electrical" x="255" y="335">Electrical</tspan>
      <tspan class="svc-air" x="410" y="300">Air Conditioning</tspan>
      <tspan class="svc-plumbing" x="670" y="278">Plumbing</tspan>
    </text>

    <g transform="rotate(-7.77 0 434)">
      <text class="phone" x="250" y="435" font-size="24" fill="var(--white)">0437205816</text>
      <text class="web" x="490" y="433" font-size="18">www.brightwellelectrical-example.com.au</text>
    </g>
  </svg>

  <!-- Layout B: straight base band -->
  <svg class="side-view side-view--b" viewBox="0 0 1100 480" aria-label="Van side layout with straight base band">
    <defs>
      <clipPath id="panel-b"><rect x="0" y="0" width="1100" height="480" rx="40"/></clipPath>
    </defs>
    <g clip-path="url(#panel-b)">
      <rect class="panel-body" x="0" y="0" width="1100" height="480" fill="var(--panel)"/>
      <path class="rear-block-orange" d="M770,0 H1100 V240 C1000,210 880,220 770,260 Z" fill="var(--orange)"/>
      <path class="rear-block-blue" d="M770,260 C880,220 1000,210 1100,240 V330 C990,300 870,300 770,330 Z" fill="var(--blue)"/>
      <rect class="band-red" x="0" y="390" width="1100" height="90" fill="var(--red)"/>
      <circle class="brand-dot" cx="910" cy="150" r="110" fill="var(--white)"/>
    </g>
    <rect x="0.5" y="0.5" width="1099" height="479" rx="40" fill="none" stroke="var(--edge)"/>

    <g class="badge">
      <text class="badge-hours" x="510" y="100" font-size="52">24/7</text>
      <text class="badge-label" x="500" y="132" font-size="24" fill="var(--blue)">Emergency</text>
      <text class="badge-label" x="540" y="158" font-size="22" fill="var(--red)">Services</text>
    </g>

    <text class="phone" x="90" y="230" font-size="26" fill="var(--blue)">0437205816</text>

    <text class="wordmark" x="255" y="320">Brightwell</text>
    <text class="services" y="372">
      <tspan class="svc-electrical" x="265">Electrical</tspan>
      <tspan class="svc-air" x="420">Air Conditioning</tspan>
      <tspan class="svc-plumbing" x="670">Plumbing</tspan>
    </text>

    <text class="web" x="280" y="428" font-size="26">www.brightwellelectrical-example.com.au</text>
  </svg>

</main>
</body>
</html>
```